TPR Letterhead

We need a letterhead design that will be able to be used on all marketing products (letterhead, mail chimp, envelops, business cards, etc.) We are a law firm specializing primarily in transportation law but offer a wide range of services to our clients. We would like the design to be modern, simple, and professional. Our colors are black and gold, however, we've incorporated dark gray and white on other marketing products such as our website.

```html
<!DOCTYPE html>
<html lang="en">
<head>
<meta charset="utf-8">
<title>TPR Law Group – Business Cards</title>
<link rel="stylesheet" href="https://fonts.googleapis.com/css2?family=Arimo:wght@400&family=Cinzel:wght@400;700&display=swap">
<style>
  :root {
    --backdrop: #cdcdcd;
    --gold: #b89b72;
    --gold-deep: #3b3022;
    --black: #000000;
    --white: #ffffff;
    --rule: #6b5a42;
  }
  * { margin: 0; padding: 0; box-sizing: border-box; }
  html, body { width: 1200px; height: 802px; overflow: hidden; }
  body { background: var(--backdrop); position: relative; font-family: "Arimo", Arial, sans-serif; }

  .card {
    position: absolute;
    top: 274px;
    width: 442px;
    height: 265px;
    overflow: hidden;
    box-shadow: 2px 3px 6px rgba(0,0,0,.35);
  }
  .card--contact { left: 136px; background: var(--gold); }
  .card--brand { left: 624px; background: var(--black); }

  .card__pattern {
    position: absolute; inset: 0;
    background: radial-gradient(ellipse 62% 78% at 50% 38%, var(--gold) 62%, var(--gold-deep) 100%);
  }

  .contact { position: absolute; inset: 0; text-align: center; color: var(--black); }
  .contact__name {
    position: absolute; left: 0; right: 0; top: 52px;
    font-family: "Cinzel", Georgia, serif; font-weight: 700; font-size: 15.5px; line-height: 1.1; letter-spacing: .3px;
  }
  .contact__role { position: absolute; left: 0; right: 0; top: 69px; font-size: 12px; line-height: 1.1; }
  .contact__rule { position: absolute; height: 1px; background: var(--rule); }
  .contact__rule--top { left: 151px; width: 140px; top: 102px; }
  .contact__rule--bottom { left: 153px; width: 142px; top: 175px; }
  .contact__icons {
    position: absolute; left: 191px; top: 94px; width: 62px; height: 16px;
    display: flex; justify-content: space-between;
  }
  .contact__icons svg { width: 16px; height: 16px; display: block; }
  .contact__line { position: absolute; left: 0; right: 0; font-size: 12.3px; line-height: 1; }
  .contact__line--phone { top: 120px; }
  .contact__line--email { top: 137px; }
  .contact__line--web { top: 153px; }
  .contact__line--street { top: 185px; }
  .contact__line--city { top: 201px; }

  .brand { position: absolute; inset: 0; text-align: center; color: var(--white); font-family: "Cinzel", Georgia, serif; font-weight: 400; }
  .brand__square { position: absolute; left: 206px; top: 62px; width: 30px; height: 30px; background: var(--gold); }
  .brand__name { position: absolute; left: 0; right: 0; top: 128px; font-size: 48px; line-height: 1; letter-spacing: 1px; }
  .brand__tagline { position: absolute; left: 0; right: 0; top: 190px; font-size: 23px; line-height: 1; letter-spacing: 3px; color: var(--gold); }
</style>
</head>
<body>

  <section class="card card--contact" aria-label="Business card, contact side">
    <div class="card__pattern" role="img" aria-label="Decorative black and gold diagonal band pattern"></div>
    <div class="contact">
      <h1 class="contact__name">DANIEL REYES</h1>
      <p class="contact__role">Managing Director</p>
      <div class="contact__rule contact__rule--top"></div>
      <div class="contact__icons">
        <svg viewBox="0 0 16 16" aria-label="Phone"><rect width="16" height="16" rx="2" fill="var(--black)"/><path d="M3.5 7.5c0-2 2-3 4.5-3s4.5 1 4.5 3H10.5V6.5h-5v1z M5 8.5h6l1 4H4z" fill="var(--gold)"/></svg>
        <svg viewBox="0 0 16 16" aria-label="Email"><rect width="16" height="16" rx="2" fill="var(--black)"/><rect x="3" y="4.5" width="10" height="7" fill="var(--gold)"/><path d="M3 4.5l5 4 5-4" fill="none" stroke="var(--black)" stroke-width="1"/></svg>
        <svg viewBox="0 0 16 16" aria-label="Website"><rect width="16" height="16" rx="2" fill="var(--black)"/><circle cx="8" cy="8" r="4.6" fill="var(--gold)"/><path d="M3.4 8h9.2M8 3.4c-2 2.6-2 6.6 0 9.2M8 3.4c2 2.6 2 6.6 0 9.2" fill="none" stroke="var(--black)" stroke-width=".8"/></svg>
      </div>
      <p class="contact__line contact__line--phone">044-555 010 200</p>
      <p class="contact__line contact__line--email">info@tprlaw.com</p>
      <p class="contact__line contact__line--web">www.tprlaw.com</p>
      <div class="contact__rule contact__rule--bottom"></div>
      <p class="contact__line contact__line--street">318, Commerce Way East</p>
      <p class="contact__line contact__line--city">45210, Ohio USA</p>
    </div>
  </section>

  <section class="card card--brand" aria-label="Business card, brand side">
    <div class="brand">
      <div class="brand__square"></div>
      <p class="brand__name">TPR</p>
      <p class="brand__tagline">LAW GROUP</p>
    </div>
  </section>

</body>
</html>
```